Create a Wordpress website and online store for a car performance shop

-Website to be coded in Wordpress AFTER design and be an WooCommerce store (will increase to a proper budget for coding after design has been finalised/picked)

-We are a car performance shop that is offering mechanical services + selling parts online

Industry/Entity Type

Automotive

Logo Text

Brisk Automotive

Number of Pages Required

3 page

Colors
e24097
e667a6
eea4c8
fff9f9

Requirements
Must have
• - Wordpress with WooCommerce store
• - Similar website/store design to what i want - https://kestrunparts.com/default.aspx
• See Website script.docx attached.
• I don't want it to be exact copy but it is a inspiration of what i want my website to look/feel.
• - LOGO must be playful using the colours picked - see attached SAMPLE LOGOS.jpg

```html
<!DOCTYPE html>
<html lang="en">
<head>
<meta charset="utf-8">
<title>Brisk Automotive</title>
<link href="https://fonts.googleapis.com/css2?family=Montserrat:wght@500;600;700&family=Lato:wght@400;700&display=swap" rel="stylesheet">
<style>
:root{
  --pink:#e24097;
  --pink-deep:#d81f80;
  --pink-mid:#e667a6;
  --pink-soft:#eea4c8;
  --pink-pale:#f5d9e8;
  --pink-bar:#f9e6f0;
  --snow:#fff9f9;
  --ink:#1d1d1d;
  --line:#e2e2e2;
  --star:#f5b800;
}
*{box-sizing:border-box;margin:0;padding:0}
html,body{width:692px;height:1200px;overflow:hidden;background:#fff}
body{font-family:"Lato",sans-serif;color:var(--ink);position:relative}
.abs{position:absolute}

.topbar{left:0;top:0;width:692px;height:23px;background:var(--pink-bar);border-bottom:1px solid var(--pink-soft)}
.topbar .phone{left:69px;top:7px;font:600 8px "Montserrat",sans-serif;color:#333;display:flex;gap:3px;align-items:center}
.toplinks{right:82px;top:0;height:23px;display:flex;font:600 7px "Montserrat",sans-serif;color:#222}
.toplinks span{padding:0 7px;line-height:23px;border-left:1px solid var(--pink-soft)}
.toplinks span:first-child{border:none}

.logo{left:65px;top:40px;width:110px;font:700 19px/1.05 "Montserrat",sans-serif;color:var(--pink);display:flex;align-items:center;gap:5px}
.logo i{width:10px;height:10px;border-radius:50%;background:var(--pink);flex:none}
.search{left:234px;top:51px;width:254px;height:27px;border:1px solid var(--pink-soft);font:400 8.5px/25px "Lato",sans-serif;color:#777;padding:0 13px}
.search-btn{left:460px;top:51px;width:28px;height:27px;background:var(--pink);display:flex;align-items:center;justify-content:center}
.user{left:530px;top:51px}
.cart{left:562px;top:52px}
.badge{left:580px;top:47px;width:15px;height:15px;border-radius:50%;background:var(--pink);color:#fff;font:400 8px/15px "Lato",sans-serif;text-align:center}

.nav{left:0;top:102px;width:692px;height:36px;background:linear-gradient(var(--pink),var(--pink-deep))}
.nav .item{top:0;height:36px;font:600 10px/36px "Montserrat",sans-serif;color:#fff;display:flex;align-items:center;gap:3px}
.nav .home{left:59px;width:79px;justify-content:center;background:var(--pink-mid)}

.cats{left:60px;top:150px;width:149px;height:393px;background:var(--pink-pale)}
.cats h2{position:absolute;left:26px;top:20px;font:600 11.5px "Montserrat",sans-serif;color:#222}
.cats ul{position:absolute;left:0;top:41px;width:149px;list-style:none}
.cats li{height:26.7px;border-bottom:1px solid #cfc3c9;font:500 8.5px/26.7px "Montserrat",sans-serif;color:#222;padding-left:26px;position:relative}
.cats li:last-child{border:none}
.cats li svg{position:absolute;right:12px;top:9px}

.hero{left:220px;top:150px;width:417px;height:241px;overflow:hidden;
  background:
    radial-gradient(ellipse 120px 90px at 80% 48%,rgba(255,196,90,.85),rgba(196,110,30,.55) 45%,transparent 80%),
    radial-gradient(ellipse 90px 70px at 62% 62%,rgba(214,130,40,.7),transparent 75%),
    radial-gradient(ellipse 80px 60px at 94% 30%,rgba(230,150,50,.6),transparent 75%),
    radial-gradient(ellipse 160px 70px at 25% 55%,rgba(90,90,90,.45),transparent 80%),
    linear-gradient(180deg,#3a3a3a 0,#1b1b1b 45%,#262626 100%)}
.hero h1{position:absolute;left:31px;top:65px;font:700 17px/21px "Montserrat",sans-serif;color:#fff}
.hero p{position:absolute;left:31px;top:114px;width:175px;font:400 8.3px/11px "Lato",sans-serif;color:#eee}
.hero .cta{position:absolute;left:33px;top:143px;width:95px;height:26px;background:var(--pink);color:#fff;font:600 9px/26px "Montserrat",sans-serif;text-align:center}
.dots{position:absolute;left:178px;top:220px;display:flex;gap:3px;align-items:center}
.dots b{width:5px;height:5px;border-radius:50%;background:#999}
.dots b.on{background:#fff}
.dots .arr{width:10px;height:10px;border-radius:50%;background:#fff;display:flex;align-items:center;justify-content:center}

.section-title{font:700 11.5px "Montserrat",sans-serif;text-align:center}
.brand{width:79px;height:47px;border:1px solid var(--line);display:flex;align-items:center;justify-content:center;font:700 8.5px "Montserrat",sans-serif;color:#666;text-align:center}
.brand.all{color:var(--pink);font-size:7.5px;line-height:10px}

.mech{left:60px;top:556px;width:147px;height:399px;border:1px solid #ccc}
.mech-head{position:absolute;left:0;top:0;width:145px;height:39px;background:#e88ec0;color:#fff;font:700 11px/12px "Montserrat",sans-serif;padding:8px 20px}
.tile{position:absolute;left:8px;width:129px;height:81px;color:#fff;font:600 8.5px/12px "Montserrat",sans-serif;padding:49px 11px 0;text-shadow:0 1px 2px rgba(0,0,0,.6)}
.t1{top:49px;background:radial-gradient(ellipse 50px 30px at 72% 30%,#3fe0d0,transparent 80%),radial-gradient(ellipse 70px 50px at 85% 70%,#e0203a,transparent 80%),linear-gradient(135deg,#8a0f22,#1a2f3e 70%,#0d1a22)}
.t2{top:136px;background:radial-gradient(ellipse 50px 40px at 62% 30%,#3a5db0,transparent 80%),radial-gradient(ellipse 60px 45px at 20% 25%,#8d8d92,transparent 80%),linear-gradient(135deg,#5a5a62,#1f3a86 65%,#2a4a9a)}
.t3{top:222px;background:radial-gradient(ellipse 40px 30px at 30% 30%,#9fc0dc,transparent 80%),radial-gradient(ellipse 50px 35px at 75% 60%,#a9c2d6,transparent 80%),linear-gradient(135deg,#1f3b5a,#4e7396 50%,#253e58)}
.t4{top:309px;background:radial-gradient(ellipse 60px 25px at 20% 20%,#ffd29a,transparent 80%),radial-gradient(ellipse 55px 25px at 65% 55%,#1a1a20,transparent 85%),linear-gradient(180deg,#f0a06a,#b8603e 45%,#4a3a40 75%,#8a8a94)}

.card{width:134px;height:173px;border:1px solid var(--line)}
.card .pic{position:absolute;left:10px;top:12px;width:114px;height:92px}
.p1{background:radial-gradient(ellipse 50px 42px at 50% 50%,#b9b9bd,#dcdcdf 55%,#fff 100%)}
.p2{background:radial-gradient(ellipse 30px 22px at 25% 55%,#3a3a3a,transparent 90%),radial-gradient(ellipse 40px 30px at 55% 38%,#8e8e92,transparent 90%),radial-gradient(ellipse 28px 22px at 80% 58%,#4a4a4a,transparent 90%),#fff}
.p3{background:radial-gradient(circle 36px at 55% 45%,#6c6c70,#a0a0a5 45%,#d8d8dc 75%,#fff 100%)}
.p4{background:radial-gradient(ellipse 16px 40px at 25% 50%,#2a2a2a,transparent 90%),radial-gradient(ellipse 40px 38px at 62% 48%,#9a9aa0,transparent 90%),radial-gradient(ellipse 20px 28px at 85% 58%,#c8c8cc,transparent 90%),#fff}
.p5{background:radial-gradient(ellipse 22px 20px at 68% 20%,#e0272a,transparent 90%),radial-gradient(circle 40px at 47% 50%,#1a1a1a 0,#1a1a1a 30%,#b0b0b4 45%,#d6d6da 85%,#fff 100%)}
.p6{background:radial-gradient(circle 38px at 50% 50%,#fff 0,#fff 22%,#3a3330 32%,#5a4b42 60%,#6e5e52 85%,#fff 100%)}
.card .name{position:absolute;left:15px;top:119px;font:500 9px "Montserrat",sans-serif;color:#222}
.card .stars{position:absolute;left:14px;top:132px;font-size:7.5px;letter-spacing:-.5px;color:var(--star)}
.card .stars span{color:#f7e08a}
.card .price{position:absolute;left:14px;top:147px;font:500 11.5px "Montserrat",sans-serif;color:#333}
.card .buy{position:absolute;left:67px;top:146px;width:56px;height:16px;background:var(--pink);color:#fff;font:600 6.5px/16px "Montserrat",sans-serif;text-align:center}

.footer{left:0;top:990px;width:692px;height:210px;background:var(--pink-deep);color:#fff}
.footer h3{position:absolute;top:35px;font:600 10.5px "Montserrat",sans-serif}
.footer .txt{position:absolute;font:400 8.5px/13px "Lato",sans-serif;color:#fff}
.ic{display:inline-flex;width:16px;height:16px;border:1px solid #fff;border-radius:50%;vertical-align:middle;margin-right:6px}
.card-shape{position:absolute;top:134px;width:19px;height:12px;border-radius:2px;background:#f3f3f7}
.email{position:absolute;left:347px;top:76px;width:149px;height:24px;border-radius:12px;background:#fff;color:#555;font:400 8px/24px "Lato",sans-serif;padding-left:12px}
.subscribe{position:absolute;left:348px;top:106px;width:68px;height:23px;border-radius:12px;background:var(--pink-soft);font:700 7px/23px "Montserrat",sans-serif;text-align:center}
.copy{position:absolute;left:0;top:177px;width:692px;border-top:1px solid rgba(255,255,255,.25);text-align:center;font:400 8px/33px "Lato",sans-serif}
</style>
</head>
<body>

<div class="abs topbar">
  <div class="abs phone"><svg width="9" height="9" viewBox="0 0 24 24"><path fill="#e24097" d="M6.6 10.8a15 15 0 0 0 6.6 6.6l2.2-2.2a1 1 0 0 1 1-.25 11.4 11.4 0 0 0 3.6.57 1 1 0 0 1 1 1V20a1 1 0 0 1-1 1A17 17 0 0 1 3 4a1 1 0 0 1 1-1h3.5a1 1 0 0 1 1 1c0 1.25.2 2.45.57 3.6a1 1 0 0 1-.25 1z"/></svg>685-555-0142</div>
  <div class="abs toplinks"><span>CONTACT</span><span>NEWS</span><span>BLOGS</span><span>LOGIN</span></div>
</div>

<div class="abs logo"><i></i>Brisk Automotive</div>
<div class="abs search">Seach Your Product</div>
<div class="abs search-btn"><svg width="11" height="11" viewBox="0 0 24 24"><circle cx="10" cy="10" r="6.5" fill="none" stroke="#fff" stroke-width="3"/><path d="M15 15l6 6" stroke="#fff" stroke-width="3"/></svg></div>
<svg class="abs user" width="18" height="21" viewBox="0 0 18 21"><circle cx="9" cy="6" r="5" fill="none" stroke="#e24097" stroke-width="1.2"/><path d="M1 20v-3a5 5 0 0 1 5-5h6a5 5 0 0 1 5 5v3z" fill="none" stroke="#e24097" stroke-width="1.2"/></svg>
<svg class="abs cart" width="20" height="18" viewBox="0 0 20 18"><path d="M1 1h3l2.5 10h10l2-7H5" fill="none" stroke="#e24097" stroke-width="1.3"/><circle cx="8" cy="15" r="1.6" fill="none" stroke="#e24097"/><circle cx="15" cy="15" r="1.6" fill="none" stroke="#e24097"/></svg>
<div class="abs badge">0</div>

<nav class="abs nav">
  <div class="abs item home">HOME</div>
  <div class="abs item" style="left:151px">CATEGORIES <svg width="9" height="6" viewBox="0 0 9 6"><path d="M1 1l3.5 3.5L8 1" fill="none" stroke="#fff" stroke-width="1.5"/></svg></div>
  <div class="abs item" style="left:252px">ABOUT</div>
  <div class="abs item" style="left:325px">PRODUCTS</div>
  <div class="abs item" style="left:417px">BRANDS <svg width="9" height="6" viewBox="0 0 9 6"><path d="M1 1l3.5 3.5L8 1" fill="none" stroke="#fff" stroke-width="1.5"/></svg></div>
  <div class="abs item" style="left:496px">CUSTOMER SERVICE <svg width="9" height="6" viewBox="0 0 9 6"><path d="M1 1l3.5 3.5L8 1" fill="none" stroke="#fff" stroke-width="1.5"/></svg></div>
</nav>

<aside class="abs cats">
  <h2>Categories</h2>
  <ul>
    <li>Aetus augue<svg width="6" height="9" viewBox="0 0 6 9"><path d="M1 1l3.5 3.5L1 8" fill="none" stroke="#444" stroke-width="1.2"/></svg></li>
    <li>Convallis et vehicula</li>
    <li>Pt pulvinar eu ante<svg width="6" height="9" viewBox="0 0 6 9"><path d="M1 1l3.5 3.5L1 8" fill="none" stroke="#444" stroke-width="1.2"/></svg></li>
    <li>Integer orci tellus<svg width="6" height="9" viewBox="0 0 6 9"><path d="M1 1l3.5 3.5L1 8" fill="none" stroke="#444" stroke-width="1.2"/></svg></li>
    <li>Tristique vitae</li>
    <li>Consequat nec<svg width="6" height="9" viewBox="0 0 6 9"><path d="M1 1l3.5 3.5L1 8" fill="none" stroke="#444" stroke-width="1.2"/></svg></li>
    <li>Porta vel lectus<svg width="6" height="9" viewBox="0 0 6 9"><path d="M1 1l3.5 3.5L1 8" fill="none" stroke="#444" stroke-width="1.2"/></svg></li>
    <li>Nulla sit amet diam<svg width="6" height="9" viewBox="0 0 6 9"><path d="M1 1l3.5 3.5L1 8" fill="none" stroke="#444" stroke-width="1.2"/></svg></li>
    <li>Aliquam enim<svg width="6" height="9" viewBox="0 0 6 9"><path d="M1 1l3.5 3.5L1 8" fill="none" stroke="#444" stroke-width="1.2"/></svg></li>
    <li>Eui lectus cursus<svg width="6" height="9" viewBox="0 0 6 9"><path d="M1 1l3.5 3.5L1 8" fill="none" stroke="#444" stroke-width="1.2"/></svg></li>
    <li>Eu mattis laoreet</li>
    <li>Viverra sit amet</li>
    <li>Aliquam enim</li>
  </ul>
</aside>

<section class="abs hero" role="img" aria-label="Glowing engine pistons and crankshaft in front of a dark car">
  <h1>CAR PERFORMANCE<br>PARTS &amp; SERVICES</h1>
  <p>Lorem ipsum dolor sit amet consectetuer adipiscing elit Nam cursus Morbi ut</p>
  <div class="cta">SHOP NOW</div>
  <div class="dots">
    <span class="arr"><svg width="4" height="6" viewBox="0 0 4 6"><path d="M3 1L1 3l2 2" fill="none" stroke="#333"/></svg></span>
    <b class="on"></b><b></b><b></b><b></b>
    <span class="arr"><svg width="4" height="6" viewBox="0 0 4 6"><path d="M1 1l2 2-2 2" fill="none" stroke="#333"/></svg></span>
  </div>
</section>

<div class="abs section-title" style="left:220px;top:412px;width:407px;color:#111">TOP BRANDS</div>
<div class="abs brand" style="left:220px;top:438px">Apex Racing</div>
<div class="abs brand" style="left:306px;top:438px">Terrix</div>
<div class="abs brand" style="left:393px;top:438px">Voltra</div>
<div class="abs brand" style="left:479px;top:438px">Dunmore</div>
<div class="abs brand" style="left:565px;top:438px">Falcon Alloys</div>
<div class="abs brand" style="left:220px;top:497px">Orbis</div>
<div class="abs brand" style="left:306px;top:497px">Ridge Racing</div>
<div class="abs brand" style="left:393px;top:497px">Kelso</div>
<div class="abs brand" style="left:479px;top:497px">Mavra</div>
<div class="abs brand all" style="left:565px;top:497px">VIEW ALL<br>BRANDS</div>

<aside class="abs mech">
  <div class="mech-head">MECHANICAL<br>SERVICE</div>
  <div class="tile t1" role="img" aria-label="Sports car headlight lit in red and teal">PERFORMANCE<br>SERVICE</div>
  <div class="tile t2" role="img" aria-label="Mechanic working under a car bonnet">CAR REPAIR<br>SERVICE</div>
  <div class="tile t3" role="img" aria-label="Close view of a car engine bay">CAR ENGINE<br>SERVICES</div>
  <div class="tile t4" role="img" aria-label="Car driving on a road at sunset">AUTOMOTIVE<br>REPAIR</div>
</aside>

<div class="abs section-title" style="left:222px;top:568px;width:416px;color:var(--pink);font-size:12.5px">FEATURED PRODUCTS</div>

<div class="abs card" style="left:222px;top:596px"><div class="pic p1" role="img" aria-label="V-twin engine block with pistons"></div><div class="name">Product Title here</div><div class="stars">★★★★<span>★</span></div><div class="price">$25.99</div><div class="buy">BUY NOW</div></div>
<div class="abs card" style="left:366px;top:596px"><div class="pic p2" role="img" aria-label="Assorted gears, bearings and pump parts"></div><div class="name">Product Title here</div><div class="stars">★★★★<span>★</span></div><div class="price">$15.99</div><div class="buy">BUY NOW</div></div>
<div class="abs card" style="left:510px;top:596px"><div class="pic p3" role="img" aria-label="Silver alloy wheel rim"></div><div class="name">Product Title here</div><div class="stars">★★★★<span>★</span></div><div class="price">$18.99</div><div class="buy">BUY NOW</div></div>
<div class="abs card" style="left:222px;top:777px"><div class="pic p4" role="img" aria-label="Shock absorber, fan and headlamp parts"></div><div class="name">Product Title here</div><div class="stars">★★★★<span>★</span></div><div class="price">$20.99</div><div class="buy">BUY NOW</div></div>
<div class="abs card" style="left:366px;top:777px"><div class="pic p5" role="img" aria-label="Drilled brake disc with red caliper"></div><div class="name">Product Title here</div><div class="stars">★★★★<span>★</span></div><div class="price">$25.99</div><div class="buy">BUY NOW</div></div>
<div class="abs card" style="left:510px;top:777px"><div class="pic p6" role="img" aria-label="Dark toothed gear ring"></div><div class="name">Product Title here</div><div class="stars">★★★★<span>★</span></div><div class="price">$24.99</div><div class="buy">BUY NOW</div></div>

<footer class="abs footer">
  <h3 style="left:71px">CONTACT US</h3>
  <div class="txt" style="left:71px;top:60px;display:flex;gap:8px"><svg width="9" height="12" viewBox="0 0 9 12"><path d="M4.5 11S1 7 1 4.5a3.5 3.5 0 0 1 7 0C8 7 4.5 11 4.5 11z" fill="none" stroke="#fff"/><circle cx="4.5" cy="4.5" r="1.2" fill="none" stroke="#fff"/></svg><span>42 Harbor Lane #4B<br>Dallas 75201 TX</span></div>
  <div class="txt" style="left:71px;top:93px;display:flex;gap:8px;font-size:9.5px"><svg width="10" height="10" viewBox="0 0 24 24"><path fill="none" stroke="#fff" stroke-width="2" d="M6.6 10.8a15 15 0 0 0 6.6 6.6l2.2-2.2 4.6 1.3V20A17 17 0 0 1 3 4h4.5l1.3 4.6z"/></svg>(555) 214 0387</div>
  <div class="txt" style="left:71px;top:111px;display:flex;gap:8px;letter-spacing:.4px"><svg width="10" height="8" viewBox="0 0 10 8"><rect x=".5" y=".5" width="9" height="7" fill="none" stroke="#fff"/><path d="M.5.5l4.5 4 4.5-4" fill="none" stroke="#fff"/></svg>hello@briskauto.com</div>
  <div class="card-shape" style="left:73px"></div><div class="card-shape" style="left:99px"></div><div class="card-shape" style="left:126px"></div><div class="card-shape" style="left:152px"></div>

  <h3 style="left:230px">QUICK LINKS</h3>
  <div class="txt" style="left:230px;top:59px">About Us<br>Our Products<br>Best Selling<br>Repair Service<br>Brands<br>Contact Us</div>

  <h3 style="left:350px">SIGN UP TO RECEIVE EMAIL</h3>
  <div class="txt" style="left:350px;top:60px">Excepteur sint occaecat cupidatat n</div>
  <div class="email">Enter Email</div>
  <div class="subscribe">SUBSCRIBE</div>

  <h3 style="left:531px">SOCIAL</h3>
  <div class="txt" style="left:531px;top:59px;line-height:23px"><span class="ic"></span>Pagebook<br><span class="ic"></span>Chirply<br><span class="ic"></span>Circlenet</div>

  <div class="copy">Copyright © 2020 All right reserved</div>
</footer>

</body>
</html>
```